WP website design (Brenn)

We need a wordpress design for an established auction and real estate company based in Tennessee. The winning design will incorporate a professional color scheme with company logo in a clean layout. The design needs to consider that this will be developed on a responsive theme. Colors are those that will highlight the logo.

Industry/Entity Type

Real Estate

Font styles to use
Sans Serif

Colors

Designer to choose colors to be used in the design.

Requirements
Must have
• Navigation: 1) Home - with auctions as content as seen at http://vornelbidhouse.com/ 2) Current Auctions 3) Past Auctions 4) Referrals 5) Why Auction 6) About Us 7) Contact Us

Header will have logo, contact info, Social icons (Facebook, Twitter, Youtube) and tagline "Bid Smart With Brenn!' Slideshow (use stock real estate image for image) will be used either in header or content area.

Widgets: Email signup form, Upcoming Auctions, Register for Online Bidding text, testimonials

Footer will have contact info (below) smaller company logo, and the association logos attached.

```html
<!DOCTYPE html>
<html lang="en">
<head>
<meta charset="utf-8">
<title>Brenn Realty &amp; Auction LLC</title>
<link href="https://fonts.googleapis.com/css2?family=Roboto+Condensed:wght@400;700&family=Open+Sans:wght@400;600;700&display=swap" rel="stylesheet">
<style>
:root{
  --olive-dark:#3d5a1f;
  --green:#6f9a35;
  --green-light:#86ad47;
  --green-bright:#66b20d;
  --navy:#343a5e;
  --navy-dark:#262b47;
  --teal:#1e7f8f;
  --teal-dark:#0b4a5d;
  --text:#444;
  --muted:#777;
  --link:#1a6fc0;
  --border:#cfcfcf;
}
*{box-sizing:border-box;margin:0;padding:0}
html,body{width:1200px;height:2584px;overflow:hidden;background:#fff}
body{position:relative;font-family:"Open Sans",Arial,sans-serif;color:var(--text);font-size:13px}
.abs{position:absolute}
.cond{font-family:"Roboto Condensed","Arial Narrow",sans-serif}

/* top bar */
.topbar{left:0;top:0;width:1200px;height:27px;background:var(--olive-dark);color:#fff;font-size:12px;text-align:right;padding:6px 28px 0 0}
.topbar span{margin-left:12px}

/* header */
.logo{left:121px;top:59px;display:flex;align-items:center;gap:10px}
.logo-name{font-family:"Roboto Condensed",sans-serif;font-weight:700;font-size:58px;color:var(--green);letter-spacing:1px;line-height:1}
.logo-mark{width:22px;height:22px;background:var(--green)}
.logo-sub{left:121px;top:120px;font-family:"Roboto Condensed",sans-serif;font-weight:700;font-size:18px;color:var(--green)}
.touch{left:885px;top:58px;font-size:11px;font-weight:600;color:var(--navy)}
.social{display:flex;gap:8px}
.social i{display:block;width:24px;height:24px;background:var(--teal);border-radius:2px}
.social-head{left:985px;top:52px}
.tagline{right:114px;top:94px;font-family:"Roboto Condensed",sans-serif;font-weight:700;font-size:40px;color:var(--green);text-transform:uppercase;line-height:1}

/* nav */
.nav{left:0;top:171px;width:1200px;height:49px;background:var(--navy);display:flex;align-items:center;padding-left:121px;color:#fff;font-size:14px}
.nav a{color:#fff;text-decoration:none;height:49px;display:flex;align-items:center;padding:0 31px}
.nav a.active{background:var(--green-light);padding:0 30px}
.nav .sep{opacity:.9}
.navline{left:0;top:220px;width:1200px;height:9px;background:linear-gradient(var(--green-light),var(--green))}

/* hero */
.hero{left:0;top:229px;width:1200px;height:453px;background:linear-gradient(90deg,var(--teal) 0%,#1b8c9c 50%,var(--teal-dark) 100%)}
.hero-photo{left:93px;top:243px;width:1004px;height:430px;background:linear-gradient(180deg,#a8c7e0 0%,#6f9251 35%,#3f5f2a 70%,#2c4720 100%)}
.hero-caption{left:113px;top:610px;font-family:"Roboto Condensed",sans-serif;font-weight:700;font-size:36px;color:#a6e86a}
.arrow{top:446px}

/* content */
.section-title{left:98px;top:708px;font-family:"Roboto Condensed",sans-serif;font-weight:700;font-size:31px;color:var(--green)}
.pager{display:flex;gap:2px}
.pager span{background:#222;color:#fff;font-size:11px;height:26px;min-width:30px;display:flex;align-items:center;justify-content:center;padding:0 8px}
.pager .cur{background:#444}

.card{left:98px;width:614px;height:309px;border:1px solid var(--border);border-radius:12px;background:#fff}
.card-title{position:absolute;left:8px;right:8px;top:9px;height:36px;border-radius:8px;background:linear-gradient(var(--green-light),var(--green));color:#fff;font-weight:700;font-size:15px;padding:8px 10px;font-family:"Roboto Condensed",sans-serif}
.card-photo{position:absolute;left:10px;top:54px;width:230px;height:160px;background:linear-gradient(180deg,#b9cfe6 0%,#d8dde0 40%,#6c8a48 75%,#4f7033 100%)}
.card-more{position:absolute;left:10px;top:214px;width:230px;height:34px;background:var(--navy-dark);color:#fff;font-size:13px;padding:8px 0 0 22px}
.card-more svg{position:absolute;right:8px;top:4px}
.card-body{position:absolute;left:254px;top:54px;width:346px}
.card-body h3{font-family:"Roboto Condensed",sans-serif;font-size:16px;color:var(--green);font-weight:700}
.card-body p{font-size:11.5px;color:#555;line-height:1.5;margin-top:6px}
.card-body hr{border:0;border-top:1px solid #ddd;margin:12px 0 14px}
.card-body h4{font-family:"Roboto Condensed",sans-serif;font-size:16px;color:var(--green);font-weight:700}
.card-body .when{font-size:11.5px;margin-top:10px}
.card-body .when b{color:#333;margin-right:8px}
.card-body .when span{color:var(--link)}
.card-body .where{font-size:11.5px;margin-top:12px;line-height:1.4}
.card-body .where b{color:#333}
.bid-btn{position:absolute;left:254px;top:252px;width:236px;height:38px;border-radius:8px;background:linear-gradient(#93b33e,#6a8a1e);color:#fff;font-size:13px;padding:10px 0 0 14px;border:1px solid #5c7a18}
.bid-btn svg{position:absolute;right:12px;top:8px}

.results{left:106px;top:2354px;font-size:13px;color:var(--green);font-weight:600}
.results b{color:#333}

/* sidebar */
.widget{left:746px;width:342px;border:1px solid var(--border);border-radius:12px;background:#fff}
.widget-head{position:absolute;left:6px;right:6px;top:6px;height:34px;border-radius:8px 8px 0 0;background:var(--teal);color:#fff;font-family:"Roboto Condensed",sans-serif;font-weight:700;font-size:16px;padding:7px 10px}
.field{position:absolute;height:30px;border:1px solid #ccc;font-size:11px;color:#aaa;padding:7px 9px}
.go{position:absolute;background:var(--navy-dark);color:#fff;font-weight:700;font-size:16px;text-align:center;padding-top:5px}
.btn-green{position:absolute;background:var(--green-bright);color:#fff;font-weight:700;border-radius:8px;text-align:center}
.w-text{position:absolute;font-size:12px;color:#444}
.testi{position:absolute;left:12px;width:316px;font-size:11px;line-height:1.35;color:#555}
.testi h5{font-family:"Roboto Condensed",sans-serif;font-size:14px;color:var(--green);margin-bottom:4px}
.testi a{display:block;color:var(--link);text-decoration:underline;margin-top:4px}
.testi-rule{position:absolute;left:12px;width:316px;border-top:1px solid #ddd}

/* footer */
.footline{left:0;top:2413px;width:1200px;border-top:1px solid #ddd}
.foot-h{font-family:"Roboto Condensed",sans-serif;font-weight:700;font-size:15px;color:var(--green)}
.badge{display:inline-block;height:30px;background:#333;margin-right:8px}
.foot-contact{left:456px;top:2450px;font-size:11px;line-height:1.5;color:#555}
.foot-contact a{color:var(--link);text-decoration:none}
.foot-logo{left:612px;top:2452px;width:268px;height:90px;border:2px solid var(--green);display:flex;flex-direction:column;align-items:center;justify-content:center}
.foot-logo .n{font-family:"Roboto Condensed",sans-serif;font-weight:700;font-size:44px;color:var(--green);line-height:1}
.foot-logo .s{font-family:"Roboto Condensed",sans-serif;font-weight:700;font-size:15px;color:var(--green)}
.copy{left:100px;top:2530px;font-size:11px;color:#888}
</style>
</head>
<body>

<header>
  <div class="abs topbar">Call Us : (800) 555-0142<span>Create Account</span><span>|</span><span>Login</span></div>
  <div class="abs logo"><span class="logo-mark"></span><span class="logo-name">BRENN</span></div>
  <div class="abs logo-sub">Realty &amp; Auction LLC · Firm # 4417</div>
  <div class="abs touch">Get In Touch With Us</div>
  <div class="abs social social-head"><i></i><i></i><i></i></div>
  <div class="abs tagline">Bid Smart With Brenn!</div>
  <nav class="abs nav">
    <a class="active">Home</a>
    <a>Current Auctions</a><span class="sep">|</span>
    <a>Past Auctions</a><span class="sep">|</span>
    <a>Referrals</a><span class="sep">|</span>
    <a>Why Auction</a><span class="sep">|</span>
    <a>About Us</a><span class="sep">|</span>
    <a>Contact Us</a>
  </nav>
  <div class="abs navline"></div>
</header>

<section class="abs hero"></section>
<div class="abs hero-photo" role="img" aria-label="Stock photo of a brick suburban house with a lawn and tall trees"></div>
<div class="abs hero-caption">Lorel ipsum dolosr sit amet</div>
<svg class="abs arrow" style="left:56px" width="16" height="26" viewBox="0 0 16 26"><path d="M13 2 3 13l10 11" fill="none" stroke="#fff" stroke-width="3"/></svg>
<svg class="abs arrow" style="left:1112px" width="16" height="26" viewBox="0 0 16 26"><path d="M3 2l10 11L3 24" fill="none" stroke="#fff" stroke-width="3"/></svg>

<main>
  <h2 class="abs section-title">Upcoming Auctions</h2>
  <div class="abs pager" style="left:598px;top:714px"><span class="cur">1</span><span>2</span><span>Next</span></div>

  <!-- auction cards -->
  <article class="abs card" style="top:754px">
    <div class="card-title">Lorem ipsum dolor sit amet conse ctetur adipisicing</div>
    <div class="card-photo" role="img" aria-label="Photo of a two-storey house for auction"></div>
    <div class="card-more">Click Here for More Details<svg width="28" height="28" viewBox="0 0 28 28"><circle cx="12" cy="12" r="9" fill="none" stroke="#fff" stroke-width="3"/><path d="M18 18l7 7" stroke="#fff" stroke-width="4"/><path d="M8 12h8M12 8v8" stroke="#fff" stroke-width="2"/></svg></div>
    <div class="card-body">
      <h3>Lorem ipsum dolor sit amet conse ctetur adipisicing</h3>
      <p>Duis aute irure dolor in reprehenderit in voluptate velit esse cillum dolore eu fugiat.</p>
      <hr>
      <h4>Live Off-site Auction with Online Bidding</h4>
      <div class="when"><b>Begins:</b><span>Tuesday, December 23, 2014 at 1:00 PM EST</span></div>
      <div class="where"><b>Location:</b><br>P.O. Box 40512<br>Millbrook, TN 37021</div>
    </div>
    <div class="bid-btn">Click Here for Online Bidding<svg width="26" height="22" viewBox="0 0 26 22"><rect x="2" y="2" width="22" height="14" fill="none" stroke="#fff" stroke-width="2.5"/><path d="M9 20h8M13 16v4" stroke="#fff" stroke-width="2.5"/></svg></div>
  </article>

  <article class="abs card" style="top:1072px">
    <div class="card-title">Lorem ipsum dolor sit amet conse ctetur adipisicing</div>
    <div class="card-photo" role="img" aria-label="Photo of a two-storey house for auction"></div>
    <div class="card-more">Click Here for More Details<svg width="28" height="28" viewBox="0 0 28 28"><circle cx="12" cy="12" r="9" fill="none" stroke="#fff" stroke-width="3"/><path d="M18 18l7 7" stroke="#fff" stroke-width="4"/><path d="M8 12h8M12 8v8" stroke="#fff" stroke-width="2"/></svg></div>
    <div class="card-body">
      <h3>Lorem ipsum dolor sit amet conse ctetur adipisicing</h3>
      <p>Duis aute irure dolor in reprehenderit in voluptate velit esse cillum dolore eu fugiat.</p>
      <hr>
      <h4>Live Off-site Auction with Online Bidding</h4>
      <div class="when"><b>Begins:</b><span>Tuesday, December 23, 2014 at 1:00 PM EST</span></div>
      <div class="where"><b>Location:</b><br>P.O. Box 40512<br>Millbrook, TN 37021</div>
    </div>
    <div class="bid-btn">Click Here for Online Bidding<svg width="26" height="22" viewBox="0 0 26 22"><rect x="2" y="2" width="22" height="14" fill="none" stroke="#fff" stroke-width="2.5"/><path d="M9 20h8M13 16v4" stroke="#fff" stroke-width="2.5"/></svg></div>
  </article>

  <article class="abs card" style="top:1390px">
    <div class="card-title">Lorem ipsum dolor sit amet conse ctetur adipisicing</div>
    <div class="card-photo" role="img" aria-label="Photo of a two-storey house for auction"></div>
    <div class="card-more">Click Here for More Details<svg width="28" height="28" viewBox="0 0 28 28"><circle cx="12" cy="12" r="9" fill="none" stroke="#fff" stroke-width="3"/><path d="M18 18l7 7" stroke="#fff" stroke-width="4"/><path d="M8 12h8M12 8v8" stroke="#fff" stroke-width="2"/></svg></div>
    <div class="card-body">
      <h3>Lorem ipsum dolor sit amet conse ctetur adipisicing</h3>
      <p>Duis aute irure dolor in reprehenderit in voluptate velit esse cillum dolore eu fugiat.</p>
      <hr>
      <h4>Live Off-site Auction with Online Bidding</h4>
      <div class="when"><b>Begins:</b><span>Tuesday, December 23, 2014 at 1:00 PM EST</span></div>
      <div class="where"><b>Location:</b><br>P.O. Box 40512<br>Millbrook, TN 37021</div>
    </div>
    <div class="bid-btn">Click Here for Online Bidding<svg width="26" height="22" viewBox="0 0 26 22"><rect x="2" y="2" width="22" height="14" fill="none" stroke="#fff" stroke-width="2.5"/><path d="M9 20h8M13 16v4" stroke="#fff" stroke-width="2.5"/></svg></div>
  </article>

  <article class="abs card" style="top:1708px">
    <div class="card-title">Lorem ipsum dolor sit amet conse ctetur adipisicing</div>
    <div class="card-photo" role="img" aria-label="Photo of a two-storey house for auction"></div>
    <div class="card-more">Click Here for More Details<svg width="28" height="28" viewBox="0 0 28 28"><circle cx="12" cy="12" r="9" fill="none" stroke="#fff" stroke-width="3"/><path d="M18 18l7 7" stroke="#fff" stroke-width="4"/><path d="M8 12h8M12 8v8" stroke="#fff" stroke-width="2"/></svg></div>
    <div class="card-body">
      <h3>Lorem ipsum dolor sit amet conse ctetur adipisicing</h3>
      <p>Duis aute irure dolor in reprehenderit in voluptate velit esse cillum dolore eu fugiat.</p>
      <hr>
      <h4>Live Off-site Auction with Online Bidding</h4>
      <div class="when"><b>Begins:</b><span>Tuesday, December 23, 2014 at 1:00 PM EST</span></div>
      <div class="where"><b>Location:</b><br>P.O. Box 40512<br>Millbrook, TN 37021</div>
    </div>
    <div class="bid-btn">Click Here for Online Bidding<svg width="26" height="22" viewBox="0 0 26 22"><rect x="2" y="2" width="22" height="14" fill="none" stroke="#fff" stroke-width="2.5"/><path d="M9 20h8M13 16v4" stroke="#fff" stroke-width="2.5"/></svg></div>
  </article>

  <article class="abs card" style="top:2026px">
    <div class="card-title">Lorem ipsum dolor sit amet conse ctetur adipisicing</div>
    <div class="card-photo" role="img" aria-label="Photo of a two-storey house for auction"></div>
    <div class="card-more">Click Here for More Details<svg width="28" height="28" viewBox="0 0 28 28"><circle cx="12" cy="12" r="9" fill="none" stroke="#fff" stroke-width="3"/><path d="M18 18l7 7" stroke="#fff" stroke-width="4"/><path d="M8 12h8M12 8v8" stroke="#fff" stroke-width="2"/></svg></div>
    <div class="card-body">
      <h3>Lorem ipsum dolor sit amet conse ctetur adipisicing</h3>
      <p>Duis aute irure dolor in reprehenderit in voluptate velit esse cillum dolore eu fugiat.</p>
      <hr>
      <h4>Live Off-site Auction with Online Bidding</h4>
      <div class="when"><b>Begins:</b><span>Tuesday, December 23, 2014 at 1:00 PM EST</span></div>
      <div class="where"><b>Location:</b><br>P.O. Box 40512<br>Millbrook, TN 37021</div>
    </div>
    <div class="bid-btn">Click Here for Online Bidding<svg width="26" height="22" viewBox="0 0 26 22"><rect x="2" y="2" width="22" height="14" fill="none" stroke="#fff" stroke-width="2.5"/><path d="M9 20h8M13 16v4" stroke="#fff" stroke-width="2.5"/></svg></div>
  </article>

  <div class="abs results">Showing <b>4</b> of <b>20</b> results</div>
  <div class="abs pager" style="left:598px;top:2348px"><span class="cur">1</span><span>2</span><span>Next</span></div>
</main>

<aside>
  <section class="abs widget" style="top:757px;height:107px">
    <div class="widget-head">Search Auctions</div>
    <div class="field" style="left:16px;top:52px;width:272px">Search Here</div>
    <div class="go" style="left:284px;top:52px;width:42px;height:30px">Go</div>
  </section>

  <section class="abs widget" style="top:882px;height:408px">
    <div class="widget-head">Upcoming Auctions</div>
    <div class="w-text" style="left:0;width:340px;top:56px;text-align:center;font-weight:700;font-size:13px">Lorem ipsum dolor sit amet</div>
    <div class="abs" style="left:22px;top:88px;width:296px;height:192px;border:2px solid var(--navy-dark);background:linear-gradient(180deg,#7fa9d8 0%,#c9d3dc 45%,#8a8f90 70%,#3c88b8 100%)" role="img" aria-label="Photo of a modern luxury villa with a pool"></div>
    <div class="w-text" style="left:0;width:340px;top:288px;text-align:center;color:var(--green);font-size:13px">Lorem ipsum</div>
    <div class="w-text" style="left:24px;width:296px;top:304px;text-align:center;font-size:11px;line-height:1.35;color:#555">Praesent tibuluma molestie lacuenean udotonmera yhe ndr erit mauris ketyade. Mtayrtyasera ...</div>
    <div class="btn-green" style="left:30px;top:350px;width:280px;height:42px;font-size:16px;padding-top:10px;font-family:'Roboto Condensed',sans-serif">Want To see more? Click Here</div>
  </section>

  <section class="abs widget" style="top:1311px;height:286px">
    <div class="widget-head">Register for Online Bidding</div>
    <div class="w-text" style="left:24px;top:54px;font-size:11.5px">Not yet registered? Register Now. Just fill in the form.</div>
    <div class="field" style="left:24px;top:85px;width:292px">Your Name</div>
    <div class="field" style="left:24px;top:129px;width:292px">Your Email id</div>
    <div class="field" style="left:24px;top:172px;width:292px">Your Phone No</div>
    <div class="btn-green" style="left:24px;top:215px;width:80px;height:30px;font-size:12px;padding-top:7px;border-radius:12px">Submit</div>
    <div class="w-text" style="left:26px;top:256px;font-size:11.5px">Already registered? <span style="color:var(--link)">Sign In</span></div>
  </section>

  <section class="abs widget" style="top:1618px;height:157px">
    <div class="widget-head">Email Subscription</div>
    <div class="w-text" style="left:24px;top:54px;font-size:11.5px">Want to getmonthly update? Subscribe us.</div>
    <div class="field" style="left:24px;top:84px;width:292px">Your email id</div>
    <div class="btn-green" style="left:24px;top:124px;width:80px;height:30px;font-size:12px;padding-top:7px;border-radius:12px">Submit</div>
  </section>

  <section class="abs widget" style="top:1807px;height:408px">
    <div class="widget-head">Testimonials</div>
    <div class="testi" style="top:54px"><h5>Dana Whitfield</h5>Praesent tibulum molestie lacuenean udotonmera yhe ndr erit mauris ketyade. Mtayrtyasera miaserai tibulum molestie lacuenean hasellus porta...<a>Read More</a></div>
    <div class="testi-rule" style="top:153px"></div>
    <div class="testi" style="top:172px"><h5>Dana Whitfield</h5>Praesent tibulum molestie lacuenean udotonmera yhe ndr erit mauris ketyade. Mtayrtyasera miaserai tibulum molestie lacuenean hasellus porta...<a>Read More</a></div>
    <div class="testi-rule" style="top:271px"></div>
    <div class="testi" style="top:290px"><h5>Dana Whitfield</h5>Praesent tibulum molestie lacuenean udotonmera yhe ndr erit mauris ketyade. Mtayrtyasera miaserai tibulum molestie lacuenean hasellus porta...<a>Read More</a></div>
  </section>
</aside>

<footer>
  <div class="abs footline"></div>
  <div class="abs foot-h" style="left:102px;top:2424px">Our Associates</div>
  <div class="abs" style="left:102px;top:2458px">
    <span class="badge" style="width:76px"></span><span class="badge" style="width:40px"></span><span class="badge" style="width:96px;background:#555"></span><span class="badge" style="width:36px"></span>
  </div>
  <div class="abs copy">© 2014, All Rights Reserved</div>

  <div class="abs foot-h" style="left:456px;top:2424px">Contact Us</div>
  <div class="abs foot-contact">Unit 8, 214 Harlow Lane<br>Millbrook<br>Tennessee<br>USA<br>Email: <a>info@brennbids.com</a><br>Website: <a>www.brennbids.com</a></div>

  <div class="abs foot-logo"><span class="n">BRENN</span><span class="s">Realty &amp; Auction LLC</span></div>

  <div class="abs foot-h" style="left:936px;top:2424px">Get In Touch With Us</div>
  <div class="abs social" style="left:942px;top:2458px"><i></i><i></i><i></i></div>
</footer>

</body>
</html>
```